A resume/portfolio website for myself

I'm an independent software contractor, architect, tech trainer. I need a web site to present myself. Many ready to use portfolio designs are too artistic and focused on presenting design skills of the person. I like a nice website but the content should be a little less graphic than if you would present a graphic designer. Content could be presentation of me, core skill qualities and services and resume. Potentially a page with my tech courses in the longer run

```html
<!DOCTYPE html>
<html lang="en">
<head>
<meta charset="utf-8">
<title>Daniel Harbo — Software Contractor</title>
<link href="https://fonts.googleapis.com/css2?family=Montserrat:wght@400;500;600;700&family=Fira+Sans:wght@400;500&display=swap" rel="stylesheet">
<style>
:root{
  --navy:#1c1e2c;
  --navy-soft:#262939;
  --accent:#f53c14;
  --white:#ffffff;
  --ink:#1a1a1a;
  --body:#555a63;
  --muted:#8a8e99;
  --ghost-dark:rgba(255,255,255,.06);
  --ghost-light:rgba(0,0,0,.07);
  --line:#c9ccd2;
}
*{margin:0;padding:0;box-sizing:border-box}
html,body{width:1200px;height:3787px;overflow:hidden}
body{font-family:"Fira Sans",sans-serif;color:var(--body);background:var(--white)}
.section{position:relative;width:1200px;overflow:hidden}
.abs{position:absolute}
.head{font-family:"Montserrat",sans-serif;text-transform:uppercase}
.accent{color:var(--accent)}
.ghost{position:absolute;left:0;right:0;text-align:center;font-family:"Montserrat",sans-serif;font-weight:700;font-size:56px;text-transform:uppercase;white-space:nowrap}
.section-title{position:absolute;left:0;right:0;text-align:center;font-family:"Montserrat",sans-serif;font-size:35px;text-transform:uppercase;letter-spacing:.5px}
.section-title b{font-weight:700}
.section-title span{font-weight:500}

/* hero */
.hero{height:557px;background:var(--navy);color:var(--white)}
.logo{left:66px;top:24px;font-family:"Montserrat",sans-serif;font-size:24px;letter-spacing:.5px}
.logo b{font-weight:700}
.logo .sep{margin:0 10px;font-weight:400}
.logo .last{color:var(--accent);font-weight:400}
.nav{left:415px;top:32px;display:flex;gap:19px;font-family:"Montserrat",sans-serif;font-weight:600;font-size:12px}
.nav a{color:var(--white);text-decoration:none;position:relative}
.nav a.active{color:var(--accent)}
.nav a.active::after{content:"";position:absolute;left:0;right:0;top:30px;height:2px;background:var(--accent)}
.hero-phone{left:975px;top:30px;color:var(--accent);font-family:"Montserrat",sans-serif;font-weight:500;font-size:17px;display:flex;align-items:center;gap:5px}
.hero-photo{left:618px;top:73px;width:582px;height:484px;background:radial-gradient(ellipse at 60% 35%,#bdbdbd 0%,#8e8e8e 35%,#3a3c47 70%,var(--navy) 100%)}
.hero h1{left:112px;top:153px;font-family:"Montserrat",sans-serif;font-weight:500;font-size:42px;line-height:52px;text-transform:uppercase}
.hero h1 strong{display:block;color:var(--accent);font-weight:700;font-size:44px}
.hero-text{left:112px;top:272px;font-size:16px;line-height:26px;color:#e6e7ea}
.btn-outline{left:112px;top:347px;width:154px;height:46px;border:1.5px solid var(--white);display:flex;align-items:center;justify-content:center;font-family:"Montserrat",sans-serif;font-weight:700;font-size:16px}
.hero-social{left:112px;top:506px;display:flex;gap:50px;font-size:10px;color:#c9cbd1}
.hero-ghost{left:170px;top:490px;font-family:"Montserrat",sans-serif;font-weight:500;font-size:44px;color:rgba(255,255,255,.06);letter-spacing:2px}
.scroll{left:1156px;top:258px;width:20px;height:150px}
.scroll span{position:absolute;left:4px;top:0;writing-mode:vertical-rl;font-size:8px;letter-spacing:3px;color:#aeb0b8}

/* about */
.about{height:542px}
.about-photo{left:82px;top:94px;width:462px;height:355px;background:linear-gradient(135deg,#6b5a45 0%,#b9a27f 40%,#4a3a38 75%,#2d2527 100%)}
.about .ghost-title{left:600px;top:85px;font-family:"Montserrat",sans-serif;font-weight:700;font-size:54px;color:var(--ghost-light)}
.about h2{left:600px;top:106px;font-family:"Montserrat",sans-serif;font-size:34px;color:var(--ink)}
.about h2 b{font-weight:700}
.about h2 .accent{font-weight:400}
.about p{left:600px;top:175px;width:505px;font-size:16px;line-height:26px}
.btn-solid{left:600px;top:381px;width:245px;height:52px;background:var(--accent);color:var(--white);display:flex;align-items:center;justify-content:center;font-family:"Montserrat",sans-serif;font-weight:500;font-size:16px}

/* experience */
.experience{height:729px;background:var(--navy);color:var(--white)}
.timeline-line{left:274px;top:204px;width:2px;height:410px;background:#d8d9dd}
.tl-item{left:0;width:600px;height:90px}
.tl-year{position:absolute;right:354px;top:4px;text-align:right;font-size:13px;line-height:21px}
.tl-year .range{font-family:"Montserrat",sans-serif}
.tl-year .label{font-family:"Montserrat",sans-serif;font-weight:600}
.tl-dot{position:absolute;left:270px;top:6px;width:10px;height:10px;border-radius:50%;background:var(--white)}
.tl-title{position:absolute;left:293px;top:0;font-family:"Montserrat",sans-serif;font-size:16px}
.tl-text{position:absolute;left:294px;top:35px;width:260px;font-size:14px;line-height:25px;color:#6c6f7a}
.tl-item.current .tl-year .range,.tl-item.current .tl-title{color:var(--accent)}
.tl-item.current .tl-dot{background:var(--accent)}
.tl-item.current .tl-text{color:var(--white)}
.tl-end{left:260px;top:1705px}
.exp-card{left:622px;width:418px;height:100px;background:var(--white);color:var(--ink)}
.exp-card .icon{position:absolute;left:21px;top:22px;width:58px;height:58px;background:var(--navy);display:flex;align-items:center;justify-content:center}
.exp-card .date{position:absolute;left:106px;top:26px;font-family:"Montserrat",sans-serif;font-size:12px}
.exp-card .title{position:absolute;left:106px;top:46px;font-family:"Montserrat",sans-serif;font-weight:700;font-size:21px}
.exp-card.current{background:var(--accent);color:var(--white)}
.exp-card.current .icon{background:var(--white)}

/* skills */
.skills{height:735px}
.skill{width:290px;text-align:center}
.skill svg{display:block;margin:0 auto}
.skill .pct{position:absolute;left:0;right:0;top:38px;font-family:"Montserrat",sans-serif;font-weight:500;font-size:21px;color:var(--accent)}
.skill h3{margin-top:17px;font-family:"Montserrat",sans-serif;font-weight:700;font-size:16px;color:var(--ink)}
.skill p{margin-top:10px;font-size:14px;line-height:26px;color:var(--muted)}
.other-label{left:0;right:0;top:453px;text-align:center;font-family:"Montserrat",sans-serif;font-weight:500;font-size:16px;color:var(--accent)}
.tags{left:112px;top:492px;width:968px;display:grid;grid-template-columns:repeat(4,232px);gap:16px 13px}
.tag{height:67px;border:1.5px solid var(--line);border-radius:4px;display:flex;align-items:center;justify-content:center;font-family:"Montserrat",sans-serif;font-weight:500;font-size:17px;color:var(--muted)}
.tag.featured{border-color:var(--accent);color:var(--accent)}

/* services */
.services{height:550px;background:var(--navy);color:var(--white)}
.service{top:196px;width:302px;height:262px;background:var(--white);text-align:center;color:var(--muted)}
.service svg{display:block;margin:16px auto 0}
.service h3{margin-top:12px;font-family:"Montserrat",sans-serif;font-weight:700;font-size:16px;color:var(--ink)}
.service p{margin:11px auto 0;width:250px;font-size:14px;line-height:26px}
.service.highlight h3,.service.highlight p{color:var(--accent)}

/* contact */
.contact{height:586px}
.contact-ghost{color:var(--ghost-light);font-size:60px;top:86px}
.contact-copy{left:141px;top:227px;width:490px;font-size:16px;line-height:26px}
.contact-copy .drop{margin-top:14px}
.contact-social{left:141px;top:477px;display:flex;gap:26px;font-size:16px}
.contact-photo{left:732px;top:181px;width:327px;height:365px;background:radial-gradient(ellipse at 55% 40%,#d0d0d0 0%,#9a9a9a 40%,#5c5c5c 80%,#444 100%)}

/* footer */
.footer{height:88px;background:var(--navy);color:#d6d7dc;font-family:"Montserrat",sans-serif;font-size:13px}
.footer-text{left:0;right:0;top:37px;text-align:center;word-spacing:2px}
.footer-text .sep{margin:0 24px}
</style>
</head>
<body>

<header class="section hero">
  <div class="abs hero-photo" role="img" aria-label="Portrait of Daniel Harbo in a white shirt, greyscale"></div>
  <div class="abs logo"><b>DANIEL</b><span class="sep">|</span><span class="last">HARBO</span></div>
  <nav class="abs nav">
    <a class="active">HOME</a><a>EXPERIENCE</a><a>EDUCATION</a><a>SKILLS</a><a>ABOUT US</a><a>PORTFOLIO</a><a>CONTACT</a>
  </nav>
  <div class="abs hero-phone">
    <svg width="14" height="14" viewBox="0 0 24 24" aria-hidden="true"><path fill="currentColor" d="M6.6 10.8a15.1 15.1 0 0 0 6.6 6.6l2.2-2.2c.3-.3.7-.4 1-.2 1.1.4 2.3.6 3.6.6.6 0 1 .4 1 1V20c0 .6-.4 1-1 1A17 17 0 0 1 3 4c0-.6.4-1 1-1h3.5c.6 0 1 .4 1 1 0 1.3.2 2.5.6 3.6.1.3 0 .7-.2 1z"/></svg>
    555 204 7731
  </div>
  <h1 class="abs">I'm an independent<strong>Software Contractor</strong></h1>
  <p class="abs hero-text">sed do eiusmod tempor incididunt ut labore et dolore magna aliqua<br>Ut enim ad minim veniam, commodo consequat.</p>
  <div class="abs btn-outline">GET STARTED</div>
  <div class="abs hero-ghost">CREATIVE HARBO</div>
  <div class="abs hero-social"><span>Facenote</span><span>Chirper</span><span>Linkwork</span></div>
  <div class="abs scroll">
    <span>SCROLL DOWN</span>
    <svg class="abs" style="left:0;top:108px" width="20" height="40" viewBox="0 0 20 40" aria-hidden="true"><path d="M10 0v38M3 31l7 7 7-7" stroke="#aeb0b8" stroke-width="1.2" fill="none"/></svg>
  </div>
</header>

<section class="section about">
  <div class="abs about-photo" role="img" aria-label="Daniel Harbo with two colleagues in front of a bookshelf, holding a molecular model"></div>
  <div class="abs ghost-title">ABOUT US</div>
  <h2 class="abs"><b>ABOUT</b> <b>|</b> <span class="accent">DANIEL HARBO</span></h2>
  <p class="abs">Lorem ipsum dolor sit amet, consectetur adipiscing elit, sed do eiusmod tempor incididunt ut labore et dolore magna aliqua. Ut enim ad minim veniam, quis nostrud exercitation ullamco labor is nisi ut aliquip ex ea commodo consequat. Duis aute irure dolo r in reprehenderit in voluptate velit esse cillum dolore eu fugiat nulla pariatur. Excepteur sint occaecat cupidatat non proident, sunt in culpa qui officia deserunt.</p>
  <div class="abs btn-solid">DOWNLOAD MY RESUME</div>
</section>

<section class="section experience">
  <div class="ghost" style="top:92px;color:var(--ghost-dark)">MY EXPERIENCE</div>
  <h2 class="section-title" style="top:106px"><b class="accent">EDUCATION</b> <b class="accent">|</b> <span>EXPERIENCE</span></h2>

  <div class="abs timeline-line"></div>
  <div class="abs tl-item current" style="top:193px">
    <div class="tl-year"><div class="range">(2000-2005)</div><div class="label">Lorem ipsum</div></div>
    <div class="tl-dot"></div>
    <div class="tl-title">LOREM IPSUM DOLOR</div>
    <div class="tl-text">Lorem ipsum dolor sit amet, conse ctetur adipiscing elit, sed do.</div>
  </div>
  <div class="abs tl-item" style="top:296px">
    <div class="tl-year"><div class="range">(2000-2005)</div><div class="label">Lorem ipsum</div></div>
    <div class="tl-dot"></div>
    <div class="tl-title">LOREM IPSUM DOLOR</div>
    <div class="tl-text">Lorem ipsum dolor sit amet, conse ctetur adipiscing elit, sed do.</div>
  </div>
  <div class="abs tl-item" style="top:399px">
    <div class="tl-year"><div class="range">(2000-2005)</div><div class="label">Lorem ipsum</div></div>
    <div class="tl-dot"></div>
    <div class="tl-title">LOREM IPSUM DOLOR</div>
    <div class="tl-text">Lorem ipsum dolor sit amet, conse ctetur adipiscing elit, sed do.</div>
  </div>
  <div class="abs tl-item" style="top:502px">
    <div class="tl-year"><div class="range">(2000-2005)</div><div class="label">Lorem ipsum</div></div>
    <div class="tl-dot"></div>
    <div class="tl-title">LOREM IPSUM DOLOR</div>
    <div class="tl-text">Lorem ipsum dolor sit amet, conse ctetur adipiscing elit, sed do.</div>
  </div>
  <svg class="abs" style="left:260px;top:606px" width="30" height="30" viewBox="0 0 30 30" aria-hidden="true"><circle cx="15" cy="15" r="15" fill="#f53c14"/><path d="M11 13l4 4 4-4" stroke="#fff" stroke-width="1.8" fill="none"/></svg>

  <div class="abs exp-card current" style="top:182px">
    <div class="icon"><svg width="40" height="40" viewBox="0 0 40 40" aria-hidden="true"><g fill="none" stroke="#f53c14" stroke-width="1.6"><rect x="13" y="4" width="24" height="17"/><path d="M17 10h16M17 15h10"/><circle cx="7" cy="10" r="3"/><path d="M3 22v-6h8l4 3M5 22v10M9 22v10"/><circle cx="14" cy="29" r="2"/><circle cx="22" cy="29" r="2"/><circle cx="30" cy="29" r="2"/><path d="M11 36c0-2 6-2 6 0M19 36c0-2 6-2 6 0M27 36c0-2 6-2 6 0"/></g></svg></div>
    <div class="date">2000 -2005</div><div class="title">LOREM IPSUM DOLOR</div>
  </div>
  <div class="abs exp-card" style="top:294px">
    <div class="icon"><svg width="40" height="40" viewBox="0 0 40 40" aria-hidden="true"><g fill="none" stroke="#fff" stroke-width="1.6"><rect x="13" y="4" width="24" height="17"/><path d="M17 10h16M17 15h10"/><circle cx="7" cy="10" r="3"/><path d="M3 22v-6h8l4 3M5 22v10M9 22v10"/><circle cx="14" cy="29" r="2"/><circle cx="22" cy="29" r="2"/><circle cx="30" cy="29" r="2"/><path d="M11 36c0-2 6-2 6 0M19 36c0-2 6-2 6 0M27 36c0-2 6-2 6 0"/></g></svg></div>
    <div class="date">2000 -2005</div><div class="title">LOREM IPSUM DOLOR</div>
  </div>
  <div class="abs exp-card" style="top:406px">
    <div class="icon"><svg width="40" height="40" viewBox="0 0 40 40" aria-hidden="true"><g fill="none" stroke="#fff" stroke-width="1.6"><rect x="13" y="4" width="24" height="17"/><path d="M17 10h16M17 15h10"/><circle cx="7" cy="10" r="3"/><path d="M3 22v-6h8l4 3M5 22v10M9 22v10"/><circle cx="14" cy="29" r="2"/><circle cx="22" cy="29" r="2"/><circle cx="30" cy="29" r="2"/><path d="M11 36c0-2 6-2 6 0M19 36c0-2 6-2 6 0M27 36c0-2 6-2 6 0"/></g></svg></div>
    <div class="date">2000 -2005</div><div class="title">LOREM IPSUM DOLOR</div>
  </div>
  <div class="abs exp-card" style="top:518px">
    <div class="icon"><svg width="40" height="40" viewBox="0 0 40 40" aria-hidden="true"><g fill="none" stroke="#fff" stroke-width="1.6"><rect x="13" y="4" width="24" height="17"/><path d="M17 10h16M17 15h10"/><circle cx="7" cy="10" r="3"/><path d="M3 22v-6h8l4 3M5 22v10M9 22v10"/><circle cx="14" cy="29" r="2"/><circle cx="22" cy="29" r="2"/><circle cx="30" cy="29" r="2"/><path d="M11 36c0-2 6-2 6 0M19 36c0-2 6-2 6 0M27 36c0-2 6-2 6 0"/></g></svg></div>
    <div class="date">2000 -2005</div><div class="title">LOREM IPSUM DOLOR</div>
  </div>
</section>

<section class="section skills">
  <div class="ghost" style="top:107px;color:var(--ghost-light)">OUR SKILLS</div>
  <h2 class="section-title" style="top:106px;color:var(--ink)"><b>PROFESSIONAL</b> <b>|</b> <span class="accent">SKILLS</span></h2>

  <div class="abs skill" style="left:125px;top:189px">
    <svg width="100" height="100" viewBox="0 0 100 100" aria-hidden="true"><path d="M38 4.5A47 47 0 1 0 62 4.5" fill="none" stroke="#f53c14" stroke-width="3"/></svg>
    <div class="pct">80 %</div>
    <h3>LOREM IPSUM</h3>
    <p>Lorem ipsum dolor sit amet, consectetur adipiscing elit, sed do eiusmod tempor incididunt ut labore et.</p>
  </div>
  <div class="abs skill" style="left:460px;top:189px">
    <svg width="100" height="100" viewBox="0 0 100 100" aria-hidden="true"><path d="M38 4.5A47 47 0 1 0 62 4.5" fill="none" stroke="#f53c14" stroke-width="3"/></svg>
    <div class="pct">80 %</div>
    <h3>LOREM IPSUM</h3>
    <p>Lorem ipsum dolor sit amet, consectetur adipiscing elit, sed do eiusmod tempor incididunt ut labore et.</p>
  </div>
  <div class="abs skill" style="left:795px;top:189px">
    <svg width="100" height="100" viewBox="0 0 100 100" aria-hidden="true"><path d="M38 4.5A47 47 0 1 0 62 4.5" fill="none" stroke="#f53c14" stroke-width="3"/></svg>
    <div class="pct">80 %</div>
    <h3>LOREM IPSUM</h3>
    <p>Lorem ipsum dolor sit amet, consectetur adipiscing elit, sed do eiusmod tempor incididunt ut labore et.</p>
  </div>

  <div class="abs other-label">OTHER SKILLS</div>
  <div class="abs tags">
    <div class="tag featured">LOREM IPSUM DOLOR</div>
    <div class="tag">LOREM IPSUM DOLOR</div>
    <div class="tag">LOREM IPSUM DOLOR</div>
    <div class="tag">LOREM IPSUM DOLOR</div>
    <div class="tag">LOREM IPSUM DOLOR</div>
    <div class="tag">LOREM IPSUM DOLOR</div>
    <div class="tag">LOREM IPSUM DOLOR</div>
    <div class="tag">LOREM IPSUM DOLOR</div>
  </div>
</section>

<section class="section services">
  <div class="ghost" style="top:106px;color:var(--ghost-dark)">WE PROVIDE</div>
  <h2 class="section-title" style="top:106px"><b class="accent">OUR</b> <b class="accent">|</b> <span>SERVICES</span></h2>

  <div class="abs service" style="left:107px">
    <svg width="70" height="70" viewBox="0 0 70 70" aria-hidden="true"><g fill="none" stroke="#1c1e2c" stroke-width="2"><rect x="4" y="16" width="50" height="34" rx="2"/><path d="M4 43h50M24 50l-3 10M34 50l3 10M16 60h26"/><circle cx="52" cy="16" r="7"/><circle cx="52" cy="16" r="12" stroke-dasharray="4 3"/><circle cx="24" cy="31" r="6"/></g></svg>
    <h3>SOFTWARE CONTRACTOR</h3>
    <p>Lorem ipsum dolor sit amet, consectetur adipiscing elit, sed do eiusmod tempor incididunt ut labore et dolore magna aliqua.</p>
  </div>
  <div class="abs service highlight" style="left:443px">
    <svg width="70" height="70" viewBox="0 0 70 70" aria-hidden="true"><g fill="none" stroke="#f53c14" stroke-width="2"><rect x="10" y="4" width="20" height="13" rx="2"/><path d="M16 17l-2 5 6-5"/><circle cx="20" cy="30" r="6"/><path d="M10 66V46c0-6 4-9 10-9s10 3 10 9v20M20 37v29"/><circle cx="48" cy="22" r="7"/><path d="M38 66V40c0-5 4-8 10-8s10 3 10 8v26M30 46l10-6"/></g></svg>
    <h3>TECH TRAINER</h3>
    <p>Lorem ipsum dolor sit amet, consectetur adipiscing elit, sed do eiusmod tempor incididunt ut labore et dolore magna aliqua.</p>
  </div>
  <div class="abs service" style="left:778px">
    <svg width="70" height="70" viewBox="0 0 70 70" aria-hidden="true"><g fill="none" stroke="#1c1e2c" stroke-width="2"><rect x="6" y="8" width="58" height="48" rx="2"/><path d="M6 8v52c0 3 6 3 6 0V8"/><path d="M22 40l14-12 14 12M26 37v12h20V37M33 49v-7h6v7M16 49h40"/></g></svg>
    <h3>ARCHITECT</h3>
    <p>Lorem ipsum dolor sit amet, consectetur adipiscing elit, sed do eiusmod tempor incididunt ut labore et dolore magna aliqua.</p>
  </div>
</section>

<section class="section contact">
  <div class="ghost contact-ghost">GET IN TOUCH</div>
  <h2 class="section-title" style="top:106px;color:var(--ink)"><b>CONTACT</b> <b>|</b> <span class="accent">US</span></h2>
  <div class="abs contact-copy">
    <p>Lorem ipsum dolor sit amet, consectetur adipiscing elit, sed do eiusmod tempor incididunt ut labore et dolore magna ali qua. Ut enim ad minim veniam, quis nostrud exercitation ulla mco laboris nisi ut aliquip ex ea commodo consequat. Duis aute irure dolor in reprehenderit in voluptate velit esse cillum dolore eu fugiat nulla pariatur.</p>
    <p class="drop">Drop me a line at <span class="accent">hello@danielharbo.dev</span> or<br>call me at <span class="accent">555 204 7731</span></p>
  </div>
  <div class="abs contact-social"><span>Facenote</span><span>Chirper</span><span>Linkwork</span></div>
  <div class="abs contact-photo" role="img" aria-label="Greyscale portrait of Daniel Harbo"></div>
</section>

<footer class="section footer">
  <div class="abs footer-text">( C ) Copyrights 2020 Daniel Harbo<span class="sep">|</span>All Rights Reserved</div>
</footer>

</body>
</html>
```